Stonebridge 720 Real Estate Investment Company

We need a business card designed for a real estate investment company named Stonebridge 720. We want to use red#f04a50, orange #f37122 and yellow #fbee3e as the color scheme. The logo colors will need to be modified from the current blue palette. I've attach VitalBranchly logo example that captures the color scheme we're going for for Stonebridge 720. Looking for clean Sans Serif fonts.
Contact Information for Business Card
Daniel Whitlock
Managing Partner
48613 Kessler Lane, Suite 540
Tampa, FL 33671
813-555-8740 Mobile
dwhitlock@stonebridge720.example
www.stonebridge720.example
Requirements
Must have
- Looking for creative responses.
Nice to have
- Must hit color palette... orange, red, yellow

```html
<!DOCTYPE html>
<html lang="en">
<head>
<meta charset="utf-8">
<title>Stonebridge 720 – Business Card</title>
<link rel="stylesheet" href="https://fonts.googleapis.com/css2?family=Montserrat:wght@400;500;600;800&display=swap">
<style>
  :root {
    --red: #f04a50;
    --brand-red: #e8232b;
    --orange: #f37122;
    --yellow: #fbee3e;
    --ink: #1a1a1a;
    --text: #333333;
    --muted: #9a9a9a;
    --card-dark: #1f1f1f;
    --paper: #fbfbfa;
    --stage: #e6e4e1;
  }
  * { margin: 0; padding: 0; box-sizing: border-box; }
  html, body {
    width: 1200px; height: 1200px; overflow: hidden;
    background: var(--stage);
    font-family: "Montserrat", "Helvetica Neue", Arial, sans-serif;
  }
  .card {
    position: absolute; left: 150px;
    width: 900px; height: 514px;
    border-radius: 4px;
    box-shadow: 0 10px 30px rgba(0,0,0,.18);
    overflow: hidden;
  }
  .card--back { top: 60px; background: var(--card-dark); }
  .card--front { top: 626px; background: var(--paper); }

  .wordmark {
    position: absolute;
    display: flex; align-items: center; gap: 14px;
    font-weight: 800; letter-spacing: -0.5px; white-space: nowrap;
  }
  .wordmark__dot { border-radius: 50%; background: var(--brand-red); flex: none; }
  .card--back .wordmark { left: 0; right: 0; justify-content: center; top: 200px; font-size: 54px; color: #ffffff; }
  .card--back .wordmark__dot { width: 26px; height: 26px; }
  .card--front .wordmark { right: 130px; top: 78px; font-size: 42px; color: var(--ink); }
  .card--front .wordmark__dot { width: 22px; height: 22px; }

  .back-url {
    position: absolute; left: 0; right: 0; top: 330px; text-align: center;
    font-size: 19px; letter-spacing: 1.5px; color: var(--muted); font-weight: 400;
  }
  .back-url__domain { color: var(--brand-red); }

  .rule { position: absolute; left: 392px; right: 110px; top: 214px; height: 1.5px; background: var(--ink); }

  .person { position: absolute; left: 62px; top: 192px; }
  .person__name { font-size: 30px; font-weight: 600; color: var(--brand-red); letter-spacing: .5px; }
  .person__title { font-size: 18px; color: var(--text); margin-top: 4px; }

  .address {
    position: absolute; right: 80px; top: 240px; text-align: right;
    font-size: 19px; line-height: 1.55; color: var(--text); letter-spacing: .3px;
  }

  .contacts { position: absolute; left: 62px; top: 296px; list-style: none; }
  .contacts li { display: flex; align-items: center; gap: 14px; height: 34px; font-size: 18px; color: var(--text); letter-spacing: .3px; }
  .contacts svg { width: 18px; height: 18px; flex: none; }

  .bands { position: absolute; left: 0; right: 0; bottom: 0; height: 14px; display: flex; }
  .bands span { flex: 1; }
  .band--red { background: var(--brand-red); }
  .band--orange { background: var(--orange); }
  .band--yellow { background: var(--yellow); }
</style>
</head>
<body>

<section class="card card--back">
  <div class="wordmark"><span class="wordmark__dot"></span>Stonebridge 720</div>
  <p class="back-url">www.<span class="back-url__domain">stonebridge720</span>.example</p>
</section>

<section class="card card--front">
  <div class="wordmark">Stonebridge 720<span class="wordmark__dot"></span></div>
  <div class="rule"></div>

  <div class="person">
    <h1 class="person__name">DANIEL WHITLOCK</h1>
    <p class="person__title">Managing Partner</p>
  </div>

  <address class="address" style="font-style:normal">
    48613 Kessler Lane<br>
    Suite 540 Tampa, FL 33671
  </address>

  <ul class="contacts">
    <li>
      <svg viewBox="0 0 24 24" aria-hidden="true"><path fill="var(--brand-red)" d="M6.6 10.8a15.1 15.1 0 0 0 6.6 6.6l2.2-2.2c.3-.3.7-.4 1-.2 1.1.4 2.3.6 3.6.6.6 0 1 .4 1 1V20c0 .6-.4 1-1 1A17 17 0 0 1 3 4c0-.6.4-1 1-1h3.5c.6 0 1 .4 1 1 0 1.3.2 2.5.6 3.6.1.3 0 .7-.2 1z"/></svg>
      813-555-8740
    </li>
    <li>
      <svg viewBox="0 0 24 24" aria-hidden="true"><rect x="2.5" y="5" width="19" height="14" rx="1" fill="none" stroke="var(--orange)" stroke-width="2"/><path d="M3 6l9 7 9-7" fill="none" stroke="var(--orange)" stroke-width="2"/></svg>
      dwhitlock@stonebridge720.example
    </li>
    <li>
      <svg viewBox="0 0 24 24" aria-hidden="true"><circle cx="12" cy="12" r="9.5" fill="var(--yellow)"/><path d="M2.5 12h19M12 2.5c3 3 3 16 0 19M12 2.5c-3 3-3 16 0 19" fill="none" stroke="#ffffff" stroke-width="1.4"/></svg>
      www.stonebridge720.example
    </li>
  </ul>

  <div class="bands">
    <span class="band--red"></span><span class="band--orange"></span><span class="band--yellow"></span>
  </div>
</section>

</body>
</html>
```